Business card for Tolvery Anesthesia LLC

This is for a business care for Tolvery Anesthesia LLC. Dr. Lisbeth Tolvery, CRNA, DNAP is the sole provider in the LLC. Business address is 4718 N Brackley Street,
Oakhaven, PA 17342
CRNA stands for certified registered nurse anesthetist
"Calm care from first breath to waking"
I plan to give this business card to the patients that I provide anesthesia to.
Creative design that ties into Anesthesia. Calm soothing colors.

Target Market(s)

Business card for my patients.

Industry/Entity Type

Medicine

Contact Information for Business Card

Creative, professional, eye catching

Logo Text

Tolvery Anesthesia

Font styles to use
Serif
Script

Colors

Designer to choose colors to be used in the design.

Requirements
Must have
• Tolvery Anesthesia
• Dr. Lisbeth Tolvery, CRNA, DNAP
• tolvery.anesthesia@ quillmail.net
Nice to have
• "Calm care from first breath to waking"
Should not have
• phone number

```html
<!DOCTYPE html>
<html lang="en">
<head>
<meta charset="utf-8">
<title>Tolvery Anesthesia LLC – Business Card</title>
<link href="https://fonts.googleapis.com/css2?family=Open+Sans:ital,wght@0,400;0,700;1,700&display=swap" rel="stylesheet">
<style>
  :root {
    --green: #2ebf72;
    --green-light: #5fd394;
    --green-dark: #177a45;
    --green-strip: #4f9e6e;
    --mint: #bff0d6;
    --logo-green: #2f8f5c;
    --burgundy: #7d1c30;
    --orange: #eea23a;
    --ink: #2e3a36;
    --white: #ffffff;
  }
  html, body {
    margin: 0;
    padding: 0;
    width: 1200px;
    height: 777px;
    overflow: hidden;
    background: var(--white);
  }
  .card {
    display: block;
    width: 1200px;
    height: 777px;
  }
  .brand-name {
    font-family: "Open Sans", sans-serif;
    font-weight: 400;
    font-size: 31px;
    letter-spacing: 2px;
    fill: var(--logo-green);
  }
  .tagline {
    font-family: "Open Sans", sans-serif;
    font-style: italic;
    font-weight: 700;
    font-size: 19px;
    letter-spacing: 1.8px;
    fill: var(--ink);
  }
  .provider-name {
    font-family: "Open Sans", sans-serif;
    font-size: 44px;
    fill: var(--burgundy);
    letter-spacing: -0.5px;
  }
  .credentials {
    font-family: "Open Sans", sans-serif;
    font-weight: 700;
    font-size: 21px;
    letter-spacing: 2.5px;
    fill: var(--green-dark);
  }
  .contact-line {
    font-family: "Open Sans", sans-serif;
    font-size: 25px;
    letter-spacing: 2px;
    fill: var(--white);
  }
</style>
</head>
<body>
<svg class="card" viewBox="0 0 1004 650" xmlns="http://www.w3.org/2000/svg">
  <defs>
    <linearGradient id="clinicalScene" x1="0" y1="0" x2="1" y2="0">
      <stop offset="0" stop-color="#eef3f2"/>
      <stop offset="0.55" stop-color="#dfe9e8"/>
      <stop offset="0.8" stop-color="#cfe6e2"/>
      <stop offset="1" stop-color="#e9f1f0"/>
    </linearGradient>
  </defs>

  <!-- top band -->
  <rect class="top-band" x="0" y="0" width="1004" height="30" fill="var(--green)"/>

  <!-- right green field -->
  <polygon class="side-field" points="880,30 1004,30 1004,650 0,650 0,407 685,407" fill="var(--green)"/>
  <polygon class="side-accent" points="908,30 1004,30 1004,88 880,88" fill="var(--white)"/>
  <polygon class="side-accent" points="812,213 1004,213 1004,407 720,407" fill="var(--white)"/>

  <!-- header photo area -->
  <polygon class="header-photo" role="img" aria-label="Photo of a patient wearing an anesthesia mask held by gloved hands"
           points="0,30 873,30 780,213 0,213" fill="url(#clinicalScene)"/>
  <polygon class="header-chevron" points="0,150 240,150 150,213 0,213" fill="var(--mint)" opacity="0.45"/>
  <polygon class="logo-backdrop" points="0,42 580,42 560,130 0,130" fill="var(--white)" opacity="0.55"/>

  <!-- mask icon area -->
  <rect class="mask-icon" role="img" aria-label="Icon of a person breathing through an anesthesia mask"
        x="884" y="105" width="104" height="108" fill="var(--green)"/>

  <!-- company name and slogan -->
  <text class="brand-name" x="40" y="84">Tolvery Anesthesia LLC</text>
  <text class="tagline" x="70" y="118">"Calm care from first breath to waking"</text>

  <!-- provider -->
  <rect class="rule" x="30" y="236" width="457" height="2" fill="var(--orange)"/>
  <text class="provider-name" x="28" y="289">Dr.Lisbeth Tolvery</text>
  <rect class="rule" x="30" y="302" width="457" height="2" fill="var(--orange)"/>
  <text class="credentials" x="487" y="331" text-anchor="end">CRNA,DNAP</text>

  <!-- contact band -->
  <rect class="contact-strip" x="0" y="407" width="1004" height="22" fill="var(--green-light)"/>
  <polygon class="contact-strip-dark" points="0,407 880,407 869,429 0,429" fill="var(--green-strip)"/>
  <polygon class="contact-band" points="0,429 869,429 755,650 0,650" fill="var(--green-dark)"/>

  <!-- home icon -->
  <g class="icon-home" fill="var(--white)">
    <polygon points="77,459 53,480 58,484 77,467 96,484 101,480"/>
    <polygon points="61,484 77,470 93,484 93,499 82,499 82,488 72,488 72,499 61,499"/>
  </g>
  <text class="contact-line" x="164" y="478">4718 N Brackley Street,</text>
  <text class="contact-line" x="164" y="516">Oakhaven, PA 17342.</text>

  <!-- globe icon -->
  <g class="icon-globe" fill="none" stroke="var(--white)" stroke-width="2.4">
    <circle cx="77" cy="571" r="14"/>
    <ellipse cx="77" cy="571" rx="6" ry="14"/>
    <line x1="63" y1="571" x2="91" y2="571"/>
  </g>
  <text class="contact-line" x="157" y="580">tolvery.anesthesia@ quillmail.net</text>
</svg>
</body>
</html>
```